Photojournalism/photography business needs a simple, timeless & professional letterhead design

We need a letterhead design for photography/photojournalism business called 'qolvb', no capitals.

The letterhead needs to be:
- simple
- professional
- timeless
- easy to read
- consists of at least 2 colors to make it stands out.

We do mainly editorial photography, photo articles for various publications, travel, businesses, as well as people such as family and kids.

The final design should communicate professionalism, easy identification, attention grabbing, even if it has to be found among a stack of various papers on the clients' desks.

Target Market(s)

Various publications.

Industry/Entity Type

Business

Requirements
Must have
• Please use the logo attached.

```html
<!DOCTYPE html>
<html lang="en">
<head>
<meta charset="utf-8">
<title>qolvb letterhead</title>
<link rel="stylesheet" href="https://fonts.googleapis.com/css2?family=Poppins:wght@700&display=swap">
<style>
  :root {
    --backdrop: #201c1a;
    --paper: #ffffff;
    --brand-red: #d9261c;
    --brand-yellow: #f6c000;
    --brand-orange: #ee8a12;
  }
  html, body {
    margin: 0;
    padding: 0;
    overflow: hidden;
    background: var(--backdrop);
  }
  .canvas {
    position: relative;
    width: 1200px;
    height: 1020px;
    background: var(--backdrop);
    overflow: hidden;
  }
  .sheet {
    position: absolute;
    top: 115px;
    width: 558px;
    height: 790px;
    background: var(--paper);
    overflow: hidden;
  }
  .sheet--first { left: 30px; }
  .sheet--second { left: 613px; }
  .sheet svg.decor {
    position: absolute;
    left: 0;
    top: 0;
    width: 558px;
    height: 790px;
  }
  .wordmark {
    position: absolute;
    margin: 0;
    font-family: "Poppins", sans-serif;
    font-weight: 700;
    font-size: 54px;
    line-height: 1;
    letter-spacing: -1px;
    color: var(--brand-red);
  }
  .sheet--first .wordmark { left: 382px; top: 32px; }
  .sheet--second .wordmark { left: 392px; top: 705px; }
</style>
</head>
<body>
<div class="canvas">

  <section class="sheet sheet--first">
    <svg class="decor" viewBox="0 0 558 790" aria-hidden="true">
      <defs>
        <linearGradient id="header-band" x1="0" y1="0" x2="1" y2="0">
          <stop offset="0" stop-color="var(--brand-yellow)"/>
          <stop offset="0.45" stop-color="var(--brand-orange)"/>
          <stop offset="1" stop-color="var(--brand-red)"/>
        </linearGradient>
      </defs>
      <!-- header band -->
      <rect x="0" y="55" width="325" height="24" fill="url(#header-band)"/>
      <g fill="var(--brand-red)">
        <rect x="328" y="55" width="5" height="24"/>
        <rect x="336" y="55" width="5" height="24"/>
        <rect x="344" y="55" width="5" height="24"/>
        <rect x="352" y="55" width="5" height="24"/>
        <rect x="360" y="55" width="8" height="24"/>
      </g>
      <!-- footer squares -->
      <rect x="0" y="715" width="72" height="72" fill="var(--brand-red)"/>
      <rect x="74" y="715" width="2" height="75" fill="var(--brand-red)"/>
      <rect x="0" y="788" width="80" height="2" fill="var(--brand-red)"/>
      <rect x="54" y="763" width="24" height="27" fill="var(--brand-yellow)"/>
      <rect x="76" y="752" width="16" height="16" fill="var(--brand-red)"/>
      <rect x="88" y="741" width="16" height="16" fill="var(--brand-yellow)"/>
      <rect x="88" y="737" width="470" height="2" fill="var(--brand-red)"/>
    </svg>
    <p class="wordmark">qolvb</p>
  </section>

  <section class="sheet sheet--second">
    <svg class="decor" viewBox="0 0 558 790" aria-hidden="true">
      <defs>
        <linearGradient id="footer-band" x1="0" y1="0" x2="1" y2="0">
          <stop offset="0" stop-color="var(--brand-yellow)"/>
          <stop offset="0.45" stop-color="var(--brand-orange)"/>
          <stop offset="1" stop-color="var(--brand-red)"/>
        </linearGradient>
      </defs>
      <!-- header squares -->
      <rect x="0" y="0" width="72" height="72" fill="var(--brand-red)"/>
      <rect x="74" y="0" width="2" height="80" fill="var(--brand-red)"/>
      <rect x="0" y="73" width="78" height="2" fill="var(--brand-red)"/>
      <rect x="54" y="55" width="24" height="26" fill="var(--brand-yellow)"/>
      <rect x="77" y="43" width="16" height="16" fill="var(--brand-red)"/>
      <rect x="89" y="31" width="16" height="16" fill="var(--brand-yellow)"/>
      <!-- footer band -->
      <rect x="0" y="728" width="325" height="24" fill="url(#footer-band)"/>
      <g fill="var(--brand-red)">
        <rect x="328" y="728" width="5" height="24"/>
        <rect x="336" y="728" width="5" height="24"/>
        <rect x="344" y="728" width="5" height="24"/>
        <rect x="352" y="728" width="5" height="24"/>
        <rect x="360" y="728" width="8" height="24"/>
      </g>
    </svg>
    <p class="wordmark">qolvb</p>
  </section>

</div>
</body>
</html>
```